CV/Resume Design Brochure

I require a brochure design for my partner's CV (curriculum vitae or resume in US).

She is looking for work in the retail fashion sector whilst going to university.

It will be a 4 page brochure. A5 size (148mm x 210mm).

The design needs to be professional, modern and eye catching. In particular the colour scheme needs to stand out.

The contact details for the CV contents will be provided to the winning designer only.

Target Market(s)

The target audience is managers of retail stores, in particular fashion outlets.

Industry/Entity Type

Retail

Font styles to use
Serif

Colors

Designer to choose colors to be used in the design.

Requirements
Must have
• Must be eye catching in terms of design and colour, as the target audience will receive a great deal of CVs/resumes. It must also be professional and simply laid out as most managers will simply glance over it at first.
Should not have
• Complicated, intricate design that makes it look unprofessional. It should not have bland, pale colours.

```html
<!DOCTYPE html>
<html lang="en">
<head>
<meta charset="utf-8">
<title>Maren Holloway – Curriculum Vitae</title>
<link rel="stylesheet" href="https://fonts.googleapis.com/css2?family=Bodoni+Moda:ital,opsz,wght@0,6..96,400;1,6..96,400&display=swap">
<style>
  :root {
    --paper: #ede8e8;
    --ink: #111111;
    --lime: #e7f13b;
    --mint: #a9fde2;
    --illustration-dark: #2a2a2a;
    --illustration-light: #e8dccd;
    --illustration-line: #b89b7c;
  }
  * { margin: 0; padding: 0; box-sizing: border-box; }
  html, body { width: 848px; height: 1200px; overflow: hidden; background: var(--paper); }
  .page {
    position: relative;
    width: 848px;
    height: 1200px;
    background: var(--paper);
    font-family: "Bodoni Moda", "Didot", serif;
    color: var(--ink);
    overflow: hidden;
  }
  .doc-label {
    position: absolute;
    left: 91px; top: 0;
    width: 386px; height: 83px;
    background: var(--lime);
    display: flex; align-items: center;
    padding-left: 22px;
    font-style: italic;
    font-size: 44px;
    line-height: 1;
  }
  .name-band {
    position: absolute;
    left: 0; top: 0;
    width: 90px; height: 648px;
    background: var(--mint);
  }
  .name-band__text {
    position: absolute;
    left: 12px; top: 212px;
    writing-mode: vertical-rl;
    font-size: 56px;
    line-height: 1;
    white-space: nowrap;
  }
  .section-title {
    position: absolute;
    left: 133px; top: 126px;
    font-style: italic;
    font-weight: 400;
    font-size: 70px;
    line-height: 78px;
  }
  .course-list {
    position: absolute;
    left: 116px; top: 298px;
    list-style: none;
    font-size: 26px;
    line-height: 41.4px;
  }
  .course-list li { display: flex; align-items: center; }
  .course-list li::before {
    content: "";
    width: 10px; height: 10px;
    border: 1.4px solid var(--ink);
    border-radius: 50%;
    margin-right: 10px;
    flex-shrink: 0;
  }
  .dove-illustration {
    position: absolute;
    left: 470px; top: 353px;
    width: 340px; height: 232px;
    background: radial-gradient(ellipse at center, #3a3a3a 0%, #9a9696 55%, rgba(237,232,232,0) 72%);
  }
  .flower-border {
    position: absolute;
    left: 0; top: 990px;
    width: 848px; height: 210px;
    background: linear-gradient(180deg, rgba(232,220,205,0) 0%, var(--illustration-light) 45%, #f4ede4 100%);
  }
  .flower-accent {
    position: absolute;
    left: 0; top: 972px;
    width: 278px; height: 228px;
    background: linear-gradient(135deg, #f7f5f3 0%, #cfcaca 55%, var(--illustration-dark) 100%);
    border-top-right-radius: 140px;
  }
</style>
</head>
<body>
<main class="page">
  <aside class="name-band"><span class="name-band__text">Maren Holloway</span></aside>
  <div class="doc-label">curriculum vitae</div>

  <h1 class="section-title">Work Based<br>Training Courses</h1>

  <ul class="course-list">
    <li>Data Protection</li>
    <li>Basic Life Support</li>
    <li>Manual Handling</li>
    <li>Equality and Diversity</li>
    <li>Conflict Resolution</li>
    <li>Customer Comes First</li>
    <li>Deaf Awareness</li>
    <li>Fire Safety</li>
    <li>Information Governance</li>
  </ul>

  <div class="dove-illustration" role="img" aria-label="Black line drawing of a dove in flight with wings spread"></div>

  <div class="flower-border" role="img" aria-label="Row of outlined poppy flowers in soft beige along the bottom edge"></div>
  <div class="flower-accent" role="img" aria-label="Large black and white ink drawing of a poppy flower in the bottom left corner"></div>
</main>
</body>
</html>
```